Flyer für Textilien mit individueller Bestickung oder Bedruckung
Wir waren mit der Designerin hochzufrieden. Alle Änderungen und Wünsche wurden schnell und sehr kompetent bearbeitet. Sind von dem Ergebnis begeistert.
Zielgruppe
Vertrieb von Logobekleidung, wie z.B. Strickwaren, Polo Shirts und T Shirts.
Zielgruppe sind Golfclubs, Proshops, Vereine, Schulen (Schulbekleidung ), Arztpraxen sowie alle Firmen und Institutionen, die Bekleidung mit individueller Bestickung oder Bedruckung benötigen.
Aufgabenstellung
Es soll ein Flyer erstellt werden, der nicht überfrachtet ist und dem Kunden schnelle und transparente Informationen liefert. Es sollen sich möglichst viele Branchen angesprochen fühlen. Auf den grünen Button mit "golf" sollte daher verzichtet werden.
Auf unserer Internetseite www.velmax.de wird deutlich, das es zwei Geschäftsfelder in unserer Firma gibt, Golfshop einerseits und Werbetextilien andererseits. Der gewünschte Flyer soll das Thema Werbetextilien abdecken. Im Datenanhang haben wir einen von uns erstellten Flyer angehängt, der lediglich als Anhaltspunkt gelten soll. Wir begrüssen es sehr wenn der Designer sich von der Vorlage löst. Unser Logo 'velmax artline' steht für das Werbetextil Geschäft und ist gleichzeitig unsere Marke, unter der wir unsere Strickwaren produzieren.
Die Sprache sollte Deutsch sein.

```html
<!DOCTYPE html>
<html lang="de">
<head>
<meta charset="utf-8">
<title>velmax artline – Flyer Werbetextilien</title>
<link href="https://fonts.googleapis.com/css2?family=Arimo:wght@400;700&family=Michroma&display=swap" rel="stylesheet">
<style>
:root{
  --bg:#c9c9c9;
  --paper:#ffffff;
  --green:#8cbf1f;
  --green-text:#86b817;
  --ink:#3a3a3a;
  --ink-soft:#555;
  --panel-fade:#d6d7d9;
}
*{box-sizing:border-box;margin:0;padding:0}
html,body{width:976px;height:1200px;overflow:hidden}
body{background:var(--bg);font-family:"Arimo",Arial,sans-serif;color:var(--ink);position:relative}

/* Titelseite */
.cover{position:absolute;left:180px;top:30px;width:270px;height:550px;background:var(--paper);overflow:hidden}
.cover-brand{height:150px;display:flex;align-items:center;justify-content:center;font-size:30px;font-weight:400;color:var(--ink);letter-spacing:.5px}
.cover-photo{position:absolute;left:0;top:150px;width:270px;height:400px;
  background:linear-gradient(180deg,#f2f2ee 0%,#c9a98f 30%,#8e6b58 55%,#9fb86a 78%,#6f9a3a 100%)}
.cover-url{position:absolute;left:0;right:0;bottom:16px;text-align:center;color:#fff;font-weight:700;font-size:10px}

/* Innenseiten */
.spread{position:absolute;left:50px;top:624px;width:513px;height:543px;
  background:linear-gradient(180deg,var(--paper) 45%,var(--panel-fade) 100%);display:flex}
.column{position:relative;width:257px;height:100%}
.column + .column{border-left:1px solid #cfcfcf}
.visual-shirts{position:absolute;left:0;top:0;width:256px;height:220px;
  background:linear-gradient(120deg,#45b3dc 0%,#45b3dc 40%,#e8bcd6 55%,#9b4f9a 75%,#f4f4f4 100%)}
.visual-hangers{position:absolute;left:0;top:0;width:256px;height:130px;
  background:linear-gradient(180deg,#f1f3f5 0%,#e6e9ec 45%,#3a8f3c 68%,#2c9ad4 84%,#c0267f 100%)}
.section-band{position:absolute;left:0;top:129px;width:256px;height:28px;background:var(--green);opacity:.95;
  color:#fff;font-family:"Michroma",sans-serif;font-size:13px;letter-spacing:2.5px;line-height:28px;padding:0 16px;text-transform:uppercase}
.section-band.right{text-align:right}
.column-body{position:absolute;left:16px;right:16px;font-size:7.6px;line-height:1.7;color:var(--ink-soft);hyphens:auto}
.column-body.left{top:238px}
.column-body.right{top:166px}
.lead{color:var(--green-text);font-size:8.4px;line-height:1.55;text-align:justify;margin-bottom:10px}
.column-body b{color:var(--ink);font-weight:700}
.column-body p{margin-bottom:10px;text-align:justify}
.swatches{display:grid;grid-template-columns:repeat(11,1fr);gap:2px 3px;margin:6px 0 10px}
.swatch{display:flex;flex-direction:column;align-items:flex-start}
.swatch i{display:block;width:17px;height:17px;background:var(--c)}
.swatch span{font-size:2.6px;line-height:7px;color:#777;white-space:nowrap}
.facts{display:flex;gap:8px;margin-bottom:6px}
.facts .sizes{flex:0 0 106px}
.facts .delivery{flex:1}
.sizes-table{border-collapse:collapse}
.sizes-table td{padding:0 8px 0 0;line-height:1.7;white-space:nowrap;vertical-align:top}

/* Rückseite */
.back{position:absolute;left:682px;top:560px;width:255px;height:545px;background:var(--green);overflow:hidden}
.back-intro{background:var(--paper);height:200px;padding:24px 16px 0}
.back-title{font-family:"Michroma",sans-serif;color:var(--green-text);font-size:12px;letter-spacing:2.5px;text-transform:uppercase;margin-bottom:10px}
.back-intro p{font-size:7.8px;line-height:1.6;text-align:justify;hyphens:auto;margin-bottom:10px}
.claim{color:var(--green-text);font-weight:700;font-size:10.5px;text-align:center;margin-top:4px}
.shelf-photo{margin:16px auto 0;width:196px;height:132px;border:2px solid #fff;
  background:linear-gradient(90deg,#f1d93a 0%,#ef7b1f 20%,#eba7c3 38%,#d83325 55%,#c9d4ea 70%,#3f4fa5 85%,#262a4a 100%)}
.contact{padding:20px 28px 0;color:#fff;font-size:8px;line-height:1.55}
.contact-lead{margin-bottom:6px}
.contact-name{font-size:13px;font-weight:700;line-height:1.3}
.contact-person{margin-bottom:12px}
.contact-grid{display:grid;grid-template-columns:34px 1fr}
.copyright{text-align:center;font-size:4.5px;color:#fff;margin-top:18px}
</style>
</head>
<body>

<section class="cover">
  <div class="cover-brand">velmax artline</div>
  <div class="cover-photo" role="img" aria-label="Foto einer fröhlichen Familie auf dem Golfrasen neben einem Loch mit Golfball"></div>
  <div class="cover-url">www.velmax.de</div>
</section>

<section class="spread">
  <div class="column">
    <div class="visual-shirts" role="img" aria-label="Illustration von Polo-Shirts in Blau und Rosa und einem lila T-Shirt"></div>
    <div class="section-band">Shirts</div>
    <div class="column-body left">
      <p class="lead">Großes Sortiment an kurzfristig verfügbaren T-Shirts und Polo Shirts für Damen, Herren und Kinder aus Baumwolle, Mischqualität oder Funktions-Polyester.</p>
      <div><b>Farben</b>: Sehr große Farbauswahl.<br>Aktuelle Farbkarte:</div>
      <div class="swatches">
        <div class="swatch"><i style="--c:#e3231b"></i><span>tomato</span></div>
        <div class="swatch"><i style="--c:#f7f7f7"></i><span>white</span></div>
        <div class="swatch"><i style="--c:#dcd3bf"></i><span>beige</span></div>
        <div class="swatch"><i style="--c:#f3e49b"></i><span>light yellow</span></div>
        <div class="swatch"><i style="--c:#f1e030"></i><span>yellow</span></div>
        <div class="swatch"><i style="--c:#c5d52b"></i><span>acid yellow</span></div>
        <div class="swatch"><i style="--c:#16a04a"></i><span>green</span></div>
        <div class="swatch"><i style="--c:#ec6525"></i><span>dark orange</span></div>
        <div class="swatch"><i style="--c:#f4a01c"></i><span>gold yellow</span></div>
        <div class="swatch"><i style="--c:#ee7a22"></i><span>orange</span></div>
        <div class="swatch"><i style="--c:#d9211c"></i><span>red</span></div>
        <div class="swatch"><i style="--c:#e2211a"></i><span>signal red</span></div>
        <div class="swatch"><i style="--c:#4db3df"></i><span>sky blue</span></div>
        <div class="swatch"><i style="--c:#ecb9d2"></i><span>rose</span></div>
        <div class="swatch"><i style="--c:#b4a1c0"></i><span>lila</span></div>
        <div class="swatch"><i style="--c:#9c5199"></i><span>purple</span></div>
        <div class="swatch"><i style="--c:#323f95"></i><span>royal</span></div>
        <div class="swatch"><i style="--c:#2f2c72"></i><span>dark royal</span></div>
        <div class="swatch"><i style="--c:#3b2241"></i><span>aubergine</span></div>
        <div class="swatch"><i style="--c:#9fb1cf"></i><span>light blue</span></div>
        <div class="swatch"><i style="--c:#7cc8d6"></i><span>mint</span></div>
        <div class="swatch"><i style="--c:#1297c7"></i><span>turquoise</span></div>
        <div class="swatch"><i style="--c:#4a8fcd"></i><span>aqua</span></div>
        <div class="swatch"><i style="--c:#a9a9ad"></i><span>grey heather</span></div>
        <div class="swatch"><i style="--c:#97c77a"></i><span>lime green</span></div>
        <div class="swatch"><i style="--c:#138c45"></i><span>dark green</span></div>
        <div class="swatch"><i style="--c:#4f514f"></i><span>olive</span></div>
        <div class="swatch"><i style="--c:#1c1f45"></i><span>navy</span></div>
        <div class="swatch"><i style="--c:#163a52"></i><span>petrol</span></div>
        <div class="swatch"><i style="--c:#6d1e33"></i><span>wine</span></div>
        <div class="swatch"><i style="--c:#3b2612"></i><span>brown</span></div>
        <div class="swatch"><i style="--c:#45454b"></i><span>graphite</span></div>
        <div class="swatch"><i style="--c:#2a2222"></i><span>black</span></div>
      </div>
      <div class="facts">
        <div class="sizes">
          <b>Größen:</b>
          <table class="sizes-table">
            <tr><td>Herren</td><td>S – 3XL</td></tr>
            <tr><td>Damen</td><td>XS – XXL</td></tr>
            <tr><td>Kinder</td><td>98 – 164</td></tr>
          </table>
        </div>
        <div class="delivery">
          <div><b>Lieferzeit:</b> ab Lager, kurzfristig</div>
          <div style="margin-top:4px"><b>Bestickung:</b> Veredelung möglich, Mindestmenge bei Bestickung 6 Teile</div>
        </div>
      </div>
      <p><b>Preis:</b> Polo Shirts ab € 11,90 zzgl. MwSt.<br>Nach Vorlage Ihres gewünschten Stickmotives mit Größenangabe unterbreiten wir Ihnen ein individuelles Angebot zum Stickpreis.</p>
    </div>
  </div>

  <div class="column">
    <div class="visual-hangers" role="img" aria-label="Foto bunter Pullover auf weißen Kleiderbügeln an einer Stange"></div>
    <div class="section-band right">Strick</div>
    <div class="column-body right">
      <p class="lead">Merino Strickpullover und -pullunder für Damen und Herren, in feinster Qualität, 100% australische Merinowolle, bei 40% maschinenwaschbar, Total Easy Care Ausrüstung, trocknergeeignet in verschiedenen klassischen und modischen Farben.</p>
      <p><b>Größen:</b><br>Herren&nbsp;&nbsp; 48 - 58<br>Damen&nbsp;&nbsp; 36 - 48</p>
      <p><b>Info:</b> Klassische Farben während der Saison ab Lager ( je nach Saisonverlauf ) solange der Vorrat reicht. Bei modischen Farben empfehlen wir Vororder.</p>
      <p style="text-align:left">Artikel 59939 velmax artline V-Pullunder Herren<br>Artikel 59940 velmax artline V-Pullover Herren<br>Artikel 81602 velmax artline V-Pullunder Damen<br>Artikel 81603 velmax artline V-Pullover Damen</p>
      <p><b>Bestickung:</b> Veredelung möglich,<br>Mindestmenge bei Bestickung: 6 Teile</p>
      <p><b>Preis:</b> Gerne unterbreiten wir Ihnen ein individuelles Angebot.</p>
      <p><b>Referenzen:</b> Mit unseren Qualitäten sind wir seit nunmehr 15 Jahren in zahlreichen Pro Shops vertreten: GC Lauterfeld e.V., GC Mirnbach, GC Brennstal, GC Ostwiesen, GC Taldorf.</p>
    </div>
  </div>
</section>

<section class="back">
  <div class="back-intro">
    <h2 class="back-title">Über uns</h2>
    <p>Ihr Lieferant und Partner für sämtliche Logobekleidung mit Bestickung oder Bedruckung für Mitarbeiter, Vereins&shy;mannschaften, Teamausstattung, Praxisausstattung, Messebekleidung, Gastronomie, sowie Schulen und Kindergärten.</p>
    <p>Sie finden uns auch im Golf Shop Gut Arnwiesen im Golf Club Brennstal.</p>
    <div class="claim">Flexibel · Schnell · Unkompliziert</div>
  </div>
  <div class="shelf-photo" role="img" aria-label="Foto eines Regals mit gestapelten Shirts in vielen Farben"></div>
  <div class="contact">
    <div class="contact-lead">Kontaktieren Sie uns:</div>
    <div class="contact-name">Velmax Handelsvertretung</div>
    <div class="contact-person">Carla Wendorf</div>
    <div>Lindenauer Straße 14<br>68161 Rastheim</div>
    <div class="contact-grid">
      <span>Tel.:</span><span>+49 000 5550146</span>
      <span>Fax:</span><span>+49 000 5550147</span>
      <span>E-Mail:</span><span>wendorf@velmax.de</span>
      <span>Web:</span><span>www.velmax.de</span>
    </div>
    <div class="copyright">© 2014 Velmax. Alle Rechte vorbehalten.</div>
  </div>
</section>

</body>
</html>
```